Bref créative
VELMORA BUSINESS CARDS
VELMORA BC
Professional
Anselmo Tribaldes
Director General
Fidencio Lozano 4817. Local 5 Altos.
Colonia Almendros.
Nuevo Laredo, Tamaulipas 88172.
Mexico.
anselmo@velmora-ejemplo.com
www.velmora-ejemplo.com
* Importacion y Exportacion.
* Comercializacion y Procura.
* Transporte LTL, Van Trailers, Flatbed, Oversize cargo.
* Soluciones de logistica.
* Aduanas.
Vector Logo file

```html
<!DOCTYPE html>
<html lang="es">
<head>
<meta charset="utf-8">
<title>VELMORA BC — Tarjetas de presentación</title>
<link rel="stylesheet" href="https://fonts.googleapis.com/css2?family=Arimo:wght@400;700&display=swap">
<style>
  :root {
    --backdrop: #1c1d22;
    --card: #ffffff;
    --navy: #2b3383;
    --accent-yellow: #e8d84a;
    --ink: #2a2a2a;
    --ink-soft: #6a6a72;
    --name-blue: #3a4aa0;
    --rule: #c9c9d2;
  }
  * { box-sizing: border-box; margin: 0; padding: 0; }
  html, body {
    width: 1200px;
    height: 749px;
    overflow: hidden;
    background: var(--backdrop);
    font-family: "Arimo", Arial, sans-serif;
  }
  .canvas {
    position: relative;
    width: 1200px;
    height: 749px;
  }
  .card {
    position: absolute;
    width: 500px;
    height: 286px;
    background: var(--card);
    border-radius: 18px;
    overflow: hidden;
    top: 232px;
  }
  .card--front { left: 70px; }
  .card--back { left: 630px; }

  /* Front */
  .front__brand {
    position: absolute;
    left: 0; right: 0;
    top: 104px;
    text-align: center;
    font-weight: 700;
    font-size: 44px;
    letter-spacing: 1px;
    color: var(--ink);
  }
  .front__band {
    position: absolute;
    left: 0; right: 0; bottom: 0;
    height: 54px;
    background: var(--navy);
    border-top: 3px solid var(--accent-yellow);
    display: flex;
    align-items: center;
    justify-content: center;
  }
  .front__web {
    font-size: 11px;
    color: #ffffff;
    letter-spacing: 0.3px;
  }

  /* Back */
  .back__tab {
    position: absolute;
    left: 0;
    top: 64px;
    width: 16px;
    height: 158px;
    background: var(--navy);
  }
  .back__brand {
    position: absolute;
    left: 44px;
    top: 126px;
    font-weight: 700;
    font-size: 28px;
    letter-spacing: 0.5px;
    color: var(--ink);
  }
  .back__divider {
    position: absolute;
    left: 226px;
    top: 36px;
    width: 1px;
    height: 214px;
    background: var(--rule);
  }
  .back__details {
    position: absolute;
    left: 246px;
    top: 36px;
    width: 240px;
    color: var(--ink-soft);
    font-size: 10px;
    line-height: 1.45;
  }
  .back__name {
    font-size: 15px;
    color: var(--name-blue);
    line-height: 1.2;
  }
  .back__title {
    font-size: 10px;
    margin-bottom: 16px;
  }
  .back__address { margin-bottom: 18px; }
  .contact-row { display: flex; }
  .contact-row__label { width: 30px; }
</style>
</head>
<body>
<main class="canvas">
  <section class="card card--front" aria-label="Frente de la tarjeta">
    <div class="front__brand">VELMORA</div>
    <div class="front__band">
      <span class="front__web">www.velmora-ejemplo.com</span>
    </div>
  </section>

  <section class="card card--back" aria-label="Reverso de la tarjeta">
    <div class="back__tab"></div>
    <div class="back__brand">VELMORA</div>
    <div class="back__divider"></div>
    <div class="back__details">
      <p class="back__name">Anselmo Tribaldes</p>
      <p class="back__title">Director General</p>
      <p class="back__address">
        Fidencio Lozano 4817.<br>
        Local 5 Altos. Colonia Almendros.<br>
        Nuevo Laredo, Tamaulipas<br>
        88172. Mexico.
      </p>
      <p class="contact-row"><span class="contact-row__label">Phone:</span><span>555-014-2291</span></p>
      <p class="contact-row"><span class="contact-row__label">Fax:</span><span>555-014-2298</span></p>
      <p>anselmo@velmora-ejemplo.com</p>
      <p>www.velmora-ejemplo.com</p>
    </div>
  </section>
</main>
</body>
</html>
```